Business Postcard Design for Personal Training Company

Need a postcard design for my company called "Cobalt Stride" Colors are Navy Blue, Blue, Grey and White.

On the front I want there to be pictures and it to feature a box that says "Free Consultation + 50% off your first session!"

And somehow to feature the following phrases " Lose Weight. Gain Muscle."
"Customized Personal training using V-Core, the latest technology in fitness. Reach your fitness goals in just two 25-min sessions per week"

Also want featured the following phrases (maybe on back):

"up to 18 times more effective than a conventional gym workout"

I need the back of the postcard to have all my business information:

Address: 327 Venadero Ave, Building B Suite 518, Costa Mesa CA 92626
Website: cobalt-stride.example
Phone #: (949) 555-0137
E-mail: cobaltstridehealth@mailbox.example

I am going to upload my logo, before and after pictures and pictures of people training on the device. Feel free to use as many/or little photos as you want.

Target Market(s)

Wealthy Adults 40+ years old looking for a personal trainer

Industry/Entity Type

Personal Trainer

Colors
0455a3
85cae6
aaaaaa
ffffff

Requirements
Must have
• At least two of the before and after photos, and two or more photos of people working out on the device.

```html
<!DOCTYPE html>
<html lang="en">
<head>
<meta charset="utf-8">
<title>Cobalt Stride Postcard</title>
<link rel="stylesheet" href="https://fonts.googleapis.com/css2?family=Archivo+Black&family=Oswald:wght@500;600&family=Lato:wght@400;700&display=swap">
<style>
  :root {
    --cyan: #12a3dc;
    --cyan-light: #7fcdec;
    --navy: #0d6fa8;
    --grey: #9a9b9d;
    --grey-dark: #555657;
    --band: #2f3030;
    --ink: #1e1e1e;
    --white: #ffffff;
    --stage: #d4d5d7;
  }
  html, body { margin: 0; padding: 0; overflow: hidden; }
  body { width: 1200px; height: 1200px; background: var(--stage); position: relative; }
  .postcard { position: absolute; left: 259px; width: 671px; height: 521px; display: block; box-shadow: 0 10px 18px rgba(0,0,0,.25); }
  .postcard--front { top: 19px; }
  .postcard--back { top: 647px; }
  .headline-heavy { font-family: "Archivo Black", "Arial Black", sans-serif; fill: var(--cyan); }
  .headline-cond { font-family: "Oswald", "Arial Narrow", sans-serif; font-weight: 600; }
  .body-copy { font-family: "Lato", Arial, sans-serif; fill: var(--ink); }
  .brand-name { font-family: "Lato", Arial, sans-serif; font-weight: 700; fill: var(--grey-dark); letter-spacing: 2px; }
  .sub-head { font-family: "Lato", Arial, sans-serif; font-weight: 700; fill: #3a3a3a; }
  .session-label { font-family: "Lato", Arial, sans-serif; font-weight: 700; font-size: 16px; }
</style>
</head>
<body>

<!-- Front -->
<svg class="postcard postcard--front" viewBox="0 0 783 608" xmlns="http://www.w3.org/2000/svg">
  <defs>
    <linearGradient id="frontPaper" x1="0" y1="0" x2="1" y2="1">
      <stop offset="0" stop-color="#ffffff"/><stop offset="1" stop-color="#eeeeee"/>
    </linearGradient>
    <linearGradient id="rooftopPhoto" x1="0" y1="0" x2="0" y2="1">
      <stop offset="0" stop-color="#c9ccd0"/><stop offset=".35" stop-color="#6e7a70"/><stop offset=".6" stop-color="#4f7a3a"/><stop offset="1" stop-color="#3d6a2c"/>
    </linearGradient>
    <radialGradient id="badgeFill" cx=".45" cy=".4" r=".7">
      <stop offset="0" stop-color="#2db6ea"/><stop offset="1" stop-color="#0c86bf"/>
    </radialGradient>
    <clipPath id="frontClip"><rect width="783" height="608"/></clipPath>
  </defs>
  <g clip-path="url(#frontClip)">
    <rect class="card-paper" width="783" height="608" fill="url(#frontPaper)"/>
    <path d="M250 0 H783 V588 H560 C440 560 340 420 320 250 C305 130 280 50 250 0 Z" fill="var(--grey)"/>
    <path d="M250 0 H280 C330 80 345 170 350 260 C360 430 460 560 620 588 H560 C430 560 335 430 322 260 C312 150 290 60 250 0 Z" fill="var(--cyan)"/>
    <path d="M600 588 C680 570 740 540 783 500 V540 C740 570 700 585 660 588 Z" fill="var(--cyan)"/>
    <circle cx="578" cy="208" r="226" fill="none" stroke="var(--cyan)" stroke-width="8"/>
    <circle cx="578" cy="208" r="216" fill="var(--white)"/>
    <circle cx="578" cy="208" r="212" fill="url(#rooftopPhoto)" role="img" aria-label="Photo: client jumping in a training suit beside a trainer at the device, on a rooftop above a harbour"/>
    <circle cx="42" cy="110" r="9" fill="var(--cyan)"/>
    <text class="brand-name" x="60" y="118" font-size="22">COBALT STRIDE</text>
    <text class="headline-heavy" x="38" y="296" font-size="90" textLength="268" lengthAdjust="spacingAndGlyphs">LOSE</text>
    <text class="headline-heavy" x="38" y="353" font-size="60" textLength="268" lengthAdjust="spacingAndGlyphs">WEIGHT</text>
    <line x1="37" y1="366" x2="307" y2="366" stroke="var(--ink)" stroke-width="2"/>
    <text class="headline-cond" x="37" y="419" font-size="56" fill="#3e3f40" textLength="270" lengthAdjust="spacingAndGlyphs">GAIN MUSCLE</text>
    <line x1="37" y1="426" x2="307" y2="426" stroke="var(--ink)" stroke-width="2"/>
    <text class="body-copy" font-size="19">
      <tspan x="37" y="472">Customized Personal training using</tspan>
      <tspan x="37" y="495">V-Core, the latest technology in fitness.</tspan>
      <tspan x="37" y="518">Reach your fitness goals in just two</tspan>
      <tspan x="37" y="541">25-min sessions per week</tspan>
    </text>
    <circle cx="526" cy="456" r="110" fill="var(--grey)"/>
    <circle cx="526" cy="456" r="98" fill="var(--cyan-light)"/>
    <circle cx="526" cy="456" r="88" fill="url(#badgeFill)"/>
    <g class="headline-cond" fill="var(--white)" text-anchor="middle">
      <text x="526" y="428" font-size="18" font-weight="500" textLength="140" lengthAdjust="spacingAndGlyphs">FREE CONSULTATION &amp;</text>
      <text x="526" y="477" font-size="46" fill="#1b1b1b" textLength="146" lengthAdjust="spacingAndGlyphs">50% OFF</text>
      <text x="526" y="500" font-size="18" font-weight="500" textLength="140" lengthAdjust="spacingAndGlyphs">YOUR FIRST SESSION!</text>
    </g>
    <rect y="588" width="783" height="20" fill="var(--band)"/>
  </g>
</svg>

<!-- Back -->
<svg class="postcard postcard--back" viewBox="0 0 783 608" xmlns="http://www.w3.org/2000/svg">
  <defs>
    <linearGradient id="backPaper" x1="0" y1="0" x2="1" y2="1">
      <stop offset="0" stop-color="#ffffff"/><stop offset="1" stop-color="#ececec"/>
    </linearGradient>
    <linearGradient id="plankPhoto" x1="0" y1="0" x2="0" y2="1">
      <stop offset="0" stop-color="#aab0b5"/><stop offset=".45" stop-color="#5d7a4f"/><stop offset=".8" stop-color="#8aa07c"/><stop offset="1" stop-color="#f4f4f4"/>
    </linearGradient>
    <linearGradient id="blueField" x1="0" y1="0" x2="1" y2="1">
      <stop offset="0" stop-color="#3dbdee"/><stop offset="1" stop-color="#118fcb"/>
    </linearGradient>
    <linearGradient id="studioPhoto" x1="0" y1="0" x2="0" y2="1">
      <stop offset="0" stop-color="#e4e2de"/><stop offset="1" stop-color="#8b8783"/>
    </linearGradient>
    <linearGradient id="gymPhoto" x1="0" y1="0" x2="0" y2="1">
      <stop offset="0" stop-color="#dcdcdc"/><stop offset=".6" stop-color="#6f6f76"/><stop offset="1" stop-color="#3f6fc0"/>
    </linearGradient>
    <clipPath id="backClip"><rect width="783" height="608"/></clipPath>
  </defs>
  <g clip-path="url(#backClip)">
    <rect width="783" height="608" fill="url(#backPaper)"/>
    <rect x="0" y="0" width="400" height="190" fill="url(#plankPhoto)" role="img" aria-label="Photo: two women doing planks in training suits beside the device on a rooftop"/>
    <path d="M365 0 C420 90 440 200 430 320 C420 450 390 540 370 588 H783 V0 Z" fill="var(--white)"/>
    <path d="M365 0 H380 C440 100 455 220 445 330 C432 460 400 545 385 588 H370 C390 540 420 450 430 320 C440 200 420 90 365 0 Z" fill="var(--cyan)"/>
    <path d="M560 300 C640 230 720 180 783 155 V588 H390 C420 470 470 380 560 300 Z" fill="url(#blueField)"/>
    <path d="M490 380 C600 240 700 120 783 75 V135 C700 180 620 260 520 380 Z" fill="var(--grey)"/>
    <g class="headline-heavy" text-anchor="middle">
      <text x="184" y="236" font-size="36" textLength="302" lengthAdjust="spacingAndGlyphs">UP TO 18 TIMES</text>
      <text x="184" y="280" font-size="38" textLength="304" lengthAdjust="spacingAndGlyphs">MORE EFFECTIVE</text>
    </g>
    <g class="sub-head" text-anchor="middle" font-size="27">
      <text x="184" y="310">Than a conventional</text>
      <text x="184" y="339">gym workout</text>
    </g>
    <rect x="0" y="367" width="345" height="26" fill="var(--cyan)"/>
    <text class="body-copy" x="37" y="387" font-size="21" fill="var(--white)">Contact Today</text>
    <g fill="var(--navy)">
      <path d="M27 416 l4 -1 l2 4 l-2 2 a9 9 0 0 0 4 4 l2 -2 l4 2 l-1 4 c-7 0 -13 -6 -13 -13 z"/>
      <rect x="26" y="447" width="14" height="10" rx="1"/>
      <circle cx="33" cy="482" r="7"/>
      <path d="M33 506 a7 7 0 0 1 7 7 c0 5 -7 12 -7 12 s-7 -7 -7 -12 a7 7 0 0 1 7 -7 z"/>
    </g>
    <path d="M26 448 l7 5 l7 -5" fill="none" stroke="var(--white)" stroke-width="1.4"/>
    <circle cx="33" cy="513" r="2.5" fill="var(--white)"/>
    <g class="body-copy" font-size="19">
      <text x="50" y="429">(949) 555-0137</text>
      <text x="50" y="459" font-size="16" textLength="250" lengthAdjust="spacingAndGlyphs">cobaltstridehealth@mailbox.example</text>
      <text x="50" y="489">cobalt-stride.example</text>
      <text x="50" y="518">327 Venadero Ave,</text>
      <text x="50" y="541">Building B Suite 518,</text>
      <text x="50" y="564">Costa Mesa CA 92626</text>
    </g>
    <circle cx="578" cy="145" r="138" fill="var(--cyan)"/>
    <circle cx="578" cy="145" r="130" fill="var(--white)"/>
    <circle cx="578" cy="145" r="125" fill="url(#studioPhoto)" role="img" aria-label="Before and after photo: client flexing at session 1 and session 30"/>
    <line x1="575" y1="20" x2="575" y2="270" stroke="var(--white)" stroke-width="3"/>
    <rect x="470" y="215" width="210" height="28" fill="var(--white)"/>
    <text class="session-label" x="490" y="236" fill="var(--ink)">session 1</text>
    <text class="session-label" x="573" y="236" fill="var(--cyan)">|  session 30</text>

    <circle cx="428" cy="440" r="118" fill="var(--grey)"/>
    <circle cx="428" cy="440" r="108" fill="var(--white)"/>
    <circle cx="428" cy="440" r="103" fill="url(#gymPhoto)" role="img" aria-label="Photo: trainer guiding a client on an exercise ball at the device"/>

    <circle cx="643" cy="440" r="115" fill="var(--white)"/>
    <circle cx="643" cy="440" r="107" fill="url(#studioPhoto)" role="img" aria-label="Before and after photo: client at session 1 and session 30"/>
    <line x1="632" y1="333" x2="632" y2="547" stroke="#2a2a2a" stroke-width="4"/>
    <rect x="545" y="482" width="195" height="28" fill="var(--white)"/>
    <text class="session-label" x="554" y="503" fill="var(--ink)">session 1</text>
    <text class="session-label" x="634" y="503" fill="var(--cyan)">|  session 30</text>

    <rect y="588" width="783" height="20" fill="var(--band)"/>
  </g>
</svg>

</body>
</html>
```